its a new company based in Christchurch new Zealand building computers ,repairs, upgrades and anything computers for the general public,i like bright happy colours like yellows, greens reds anything that stands out and it needs to communicant trust and security towards my new company,i have no logo yet,

Target Market(s)

target market of all ages

Industry/Entity Type

Building

Contact Information for Business Card

Pixel Harbour Limited,ph-0274829315,email-brightnode47@mailvista.example,14c tamworth cl,kelvale

```html
<!DOCTYPE html>
<html lang="en">
<head>
<meta charset="utf-8">
<title>Pixel Harbour Limited – Business Card</title>
<link rel="stylesheet" href="https://fonts.googleapis.com/css2?family=Orbitron:wght@800&family=Questrial&family=Cinzel:wght@700&display=swap">
<style>
  :root {
    --page-bg: #e9ebe8;
    --card-bg: #ffffff;
    --ink: #2a2a2a;
    --ink-soft: #3c3c3c;
    --green-dark: #1f8a3c;
    --green-mid: #4cb848;
    --green-lime: #8fd12a;
    --green-pale: #c9ec8a;
    --band-text: #1d4d1f;
  }
  * { margin: 0; padding: 0; box-sizing: border-box; }
  html, body {
    width: 1200px;
    height: 801px;
    overflow: hidden;
    background: var(--page-bg);
  }
  .canvas {
    position: relative;
    width: 1200px;
    height: 801px;
  }
  .business-card {
    position: absolute;
    left: 100px;
    top: 114px;
    width: 1000px;
    height: 572px;
    background: var(--card-bg);
    overflow: hidden;
    box-shadow: 0 6px 22px rgba(0,0,0,0.15);
  }
  .pixel-field-top {
    position: absolute;
    left: 360px;
    top: 0;
    width: 640px;
    height: 120px;
    background: linear-gradient(to right, rgba(255,255,255,0) 0%, var(--green-pale) 35%, var(--green-lime) 70%, var(--green-mid) 100%);
    -webkit-mask-image: linear-gradient(to bottom, #000 40%, transparent 100%);
            mask-image: linear-gradient(to bottom, #000 40%, transparent 100%);
  }
  .company-name {
    position: absolute;
    left: 60px;
    top: 132px;
    font-family: "Orbitron", sans-serif;
    font-weight: 800;
    font-size: 68px;
    letter-spacing: 1px;
    color: var(--ink);
    white-space: nowrap;
  }
  .contact-list,
  .service-list {
    position: absolute;
    list-style: none;
    font-family: "Questrial", sans-serif;
    font-size: 22px;
    color: var(--ink-soft);
  }
  .contact-list { left: 70px; top: 236px; }
  .service-list { left: 596px; top: 232px; }
  .contact-list li,
  .service-list li {
    display: flex;
    align-items: center;
    gap: 10px;
    height: 30px;
  }
  .icon {
    width: 20px;
    height: 20px;
    flex: none;
    stroke: var(--green-mid);
    fill: none;
    stroke-width: 2;
    stroke-linecap: round;
    stroke-linejoin: round;
  }
  .divider {
    position: absolute;
    left: 566px;
    top: 226px;
    width: 3px;
    height: 100px;
    background: var(--green-mid);
  }
  .pixel-field-bottom {
    position: absolute;
    left: 0;
    top: 330px;
    width: 1000px;
    height: 130px;
    background: linear-gradient(to bottom, rgba(255,255,255,0) 0%, var(--green-pale) 40%, var(--green-lime) 75%, var(--green-dark) 100%);
  }
  .guarantee-band {
    position: absolute;
    left: 0;
    top: 460px;
    width: 1000px;
    height: 66px;
    background: var(--green-lime);
    display: flex;
    align-items: center;
    padding-left: 60px;
    font-family: "Cinzel", serif;
    font-weight: 700;
    font-size: 34px;
    letter-spacing: 2px;
    color: var(--band-text);
  }
</style>
</head>
<body>
<div class="canvas">
  <section class="business-card">
    <div class="pixel-field-top" role="img" aria-label="Decorative field of small green pixel squares"></div>

    <h1 class="company-name">PIXEL HARBOUR</h1>

    <ul class="contact-list">
      <li>
        <svg class="icon" viewBox="0 0 24 24" aria-hidden="true"><circle cx="12" cy="12" r="10"/><path d="M9 7c-1 1-1 3 1 6s4 4 5 3l1-1-2-2-1 1c-1 0-3-2-3-3l1-1-2-2z"/></svg>
        <span>027 482 9315</span>
      </li>
      <li>
        <svg class="icon" viewBox="0 0 24 24" aria-hidden="true"><rect x="3" y="6" width="18" height="12"/><path d="M3 6l9 7 9-7"/></svg>
        <span>brightnode47@mailvista.example</span>
      </li>
      <li>
        <svg class="icon" viewBox="0 0 24 24" aria-hidden="true"><path d="M3 12l9-8 9 8"/><path d="M6 10v10h12V10"/></svg>
        <span>14c tamworth cl, kelvale</span>
      </li>
    </ul>

    <div class="divider"></div>

    <ul class="service-list">
      <li>
        <svg class="icon" viewBox="0 0 24 24" aria-hidden="true"><path d="M12 3v8"/><path d="M7 6a8 8 0 1 0 10 0"/></svg>
        <span>Building Computers</span>
      </li>
      <li>
        <svg class="icon" viewBox="0 0 24 24" aria-hidden="true"><path d="M12 3v8"/><path d="M7 6a8 8 0 1 0 10 0"/></svg>
        <span>Computer Repairs</span>
      </li>
      <li>
        <svg class="icon" viewBox="0 0 24 24" aria-hidden="true"><path d="M12 3v8"/><path d="M7 6a8 8 0 1 0 10 0"/></svg>
        <span>Computer Upgrades</span>
      </li>
    </ul>

    <div class="pixel-field-bottom" role="img" aria-label="Decorative rising field of green pixel squares"></div>

    <div class="guarantee-band">100% Satisfaction Guaranteed</div>
  </section>
</div>
</body>
</html>
```